Postcard Design

We are an upscale, full service real estate boutique based in Mt. Pleasant, SC. We will be having a Grand Opening of our beautiful, new office complete with high end custom home architecture and design. I will attach photos for your review. I would like to come up with a medium postcard to be mailed to clientele of Mt. Pleasant. Home prices between $300,000 - $2.2 million. The customers can call our office for the Grand Opening Listing Promotion or stop by our grand opening. We will have drawings for door prizes that include services at Brindlecove Day Spa, Copper Kettle Pies gift certificates, and they can register to win a cruise with a listing presentation. Our Grand Opening will be a couple of different dates, April 7, 2016 and April 21, 2016. I will want an order that lists the 7th and another order that will list the 21. The look should have a very "relaxing, beach" feel, but not Myrtle Beach...should reflect colors of the ocean, like you are on vacation. I will include logos and pics for your review. Thank you!

```html
<!DOCTYPE html>
<html lang="en">
<head>
<meta charset="utf-8">
<title>Seagrove Real Estate – Grand Opening Postcard</title>
<link rel="stylesheet" href="https://fonts.googleapis.com/css2?family=Open+Sans:wght@400;600;700&family=Roboto+Condensed:wght@300;400;700&display=swap">
<style>
  :root {
    --page-bg: #ffffff;
    --frame: #3a3a3a;
    --teal: #5aa89c;
    --teal-text: #4fa398;
    --ocean-blue: #2a78b6;
    --sky-line: #5db6e2;
    --white: #ffffff;
  }
  * { margin: 0; padding: 0; box-sizing: border-box; }
  html, body {
    width: 1200px; height: 1000px; overflow: hidden;
    background: var(--page-bg);
  }
  .postcard {
    position: relative; width: 1200px; height: 1000px;
    background: var(--page-bg);
  }
  .card-frame {
    position: absolute; left: 65px; top: 84px;
    width: 1081px; height: 838px;
    border: 1.5px solid var(--frame);
  }
  .headline-band {
    position: absolute; left: 65px; top: 108px;
    width: 811px; height: 57px;
    background: var(--teal);
    color: var(--white);
    font-family: "Open Sans", sans-serif;
    font-weight: 700; font-size: 31px;
    line-height: 57px; padding-left: 58px;
    letter-spacing: 0.2px;
  }
  .brand {
    position: absolute; left: 112px; top: 192px;
    width: 230px; text-align: center;
  }
  .brand-mark { display: block; margin: 0 auto 10px; }
  .brand-name {
    font-family: "Open Sans", sans-serif;
    font-weight: 700; font-size: 27px;
    color: var(--ocean-blue); letter-spacing: 2px;
    line-height: 1.3;
  }
  .office-address {
    position: absolute; left: 357px; top: 226px;
    font-family: "Open Sans", sans-serif;
    font-weight: 400; font-size: 26px;
    color: var(--ocean-blue); line-height: 36px;
    font-style: normal;
  }
  .invitation {
    position: absolute; left: 82px; top: 390px; width: 500px;
    text-align: center;
    font-family: "Roboto Condensed", sans-serif;
    color: var(--teal-text);
  }
  .invitation-lead {
    font-weight: 300; font-size: 27px; line-height: 36px;
  }
  .invitation-lead strong { font-weight: 700; }
  .invitation-details {
    margin-top: 28px;
    font-weight: 400; font-size: 22px; line-height: 29.5px;
  }
  .invitation-details strong {
    font-weight: 700; font-size: 23px;
  }
  .address-lines {
    position: absolute; left: 635px; top: 443px; width: 466px;
  }
  .address-line {
    height: 1.5px; background: var(--sky-line);
    margin-bottom: 76px;
  }
</style>
</head>
<body>
<main class="postcard">
  <div class="card-frame"></div>

  <div class="headline-band">A REAL ESTATE BOUTIQUE OPENING SOON!</div>

  <div class="brand">
    <svg class="brand-mark" width="70" height="70" viewBox="0 0 70 70" aria-hidden="true">
      <circle cx="35" cy="35" r="33" fill="var(--ocean-blue)"/>
    </svg>
    <div class="brand-name">SEAGROVE REAL ESTATE</div>
  </div>

  <address class="office-address">
    1820 Harbor View Road<br>
    Mount Pleasant, SC 29464<br>
    Ph: 843-555-0147
  </address>

  <section class="invitation">
    <p class="invitation-lead">
      We’d love you to join us for<br>
      a lunch at our <strong>New Mt. Pleasant, SC<br>
      office on April 7th, 2016.</strong>
    </p>
    <p class="invitation-details">
      <strong>It would be a pleasure to spend<br>
      some time together!</strong><br>
      Call our office for the Grand Opening Listing<br>
      Promotion or stop by our grand opening.<br>
      You will find door prizes that include services<br>
      at Brindlecove Day Spa, Copper Kettle Pies<br>
      gift certificates, and you can register to win<br>
      a cruise with a listing presentation.
    </p>
  </section>

  <div class="address-lines">
    <div class="address-line"></div>
    <div class="address-line"></div>
    <div class="address-line"></div>
    <div class="address-line"></div>
    <div class="address-line"></div>
  </div>
</main>
</body>
</html>
```